K12 Online Learning Landing Page

We provide an Elearning site for K12 learners. I would like to redesign the landing page. The design should have a responsive view too. So I'm looking for designs that encompass the Login requirements and other links and buttons. I have attached images of the current landing page.

Target Market(s)

K12 Learners

Industry/Entity Type

Education, Training or Edtech

Font styles to use
Sans Serif

Colors

Designer to choose colors to be used in the design.

Requirements
Must have
• Login Area
Nice to have
• Menu Area, area for notices or infomation

```html
<!DOCTYPE html>
<html lang="en">
<head>
<meta charset="utf-8">
<title>Brightwick Education – Online Learning</title>
<link rel="stylesheet" href="https://fonts.googleapis.com/css2?family=Quicksand:wght@600;700&family=Nunito+Sans:wght@400;600;700&display=swap">
<style>
:root{
  --blue:#1459d9;
  --blue-dark:#0f4fc4;
  --ink:#2b2b33;
  --text:#3a3a44;
  --green:#17e24b;
  --orange:#ff9b21;
  --band:#80a9e8;
  --foot:#cddff8;
  --wave:#5e92e3;
  --wave-light:#9fc0f0;
}
*{box-sizing:border-box;margin:0;padding:0}
html,body{width:1200px;height:3000px;overflow:hidden;background:#fff}
body{font-family:"Nunito Sans",Arial,sans-serif;color:var(--text)}
.page{position:relative;width:1200px;height:3000px;overflow:hidden}
.abs{position:absolute}
.head{font-family:"Quicksand","Nunito Sans",sans-serif;font-weight:700;color:var(--ink)}
.accent{color:var(--blue)}
a{text-decoration:none;color:inherit}

.brand{left:101px;top:36px;font-family:"Quicksand",sans-serif;font-weight:700;font-size:21px;color:var(--blue)}
.menu a{position:absolute;top:42px;font-size:12px;color:var(--ink)}
.menu a.active{color:var(--blue);border-bottom:1.5px solid var(--blue);padding-bottom:3px}
.btn{position:absolute;display:flex;align-items:center;justify-content:center;font-size:12px;font-weight:600;border-radius:6px}
.btn-outline{border:1.5px solid var(--blue);color:var(--blue);background:#fff}
.btn-solid{background:var(--blue);color:#fff}
.btn-green{background:var(--green);color:#fff}
.btn-orange{background:var(--orange);color:#fff}

.hero-title{left:99px;top:128px;font-size:39px;line-height:60px;white-space:nowrap}
.hero-copy{left:100px;top:334px;width:380px;font-size:10.5px;line-height:20.5px}
.hero-copy p{margin-bottom:11px}
.learn-link{left:311px;top:524px;font-size:11.5px;color:var(--blue);border-bottom:1px solid var(--blue);display:flex;gap:6px;align-items:center}
.stat{left:99px;top:604px;font-family:"Quicksand",sans-serif;font-weight:700;font-size:30px;color:var(--ink);padding-right:6px;border-right:2px solid var(--ink);line-height:34px}
.avatars{left:175px;top:610px;display:flex}
.avatars span{width:31px;height:31px;border-radius:50%;border:2px solid #fff;margin-right:-6px}

.hero-photo{left:680px;top:170px;width:450px;height:470px;border-radius:50%;background:linear-gradient(160deg,#66e0f6 0%,#36a6dc 45%,#1c63b6 100%)}
.badge{position:absolute;width:36px;height:36px;border-radius:9px;display:flex;align-items:center;justify-content:center}

.login{left:531px;top:219px;width:216px;height:262px;border-radius:14px;background:linear-gradient(120deg,#b3b3b5 0%,#a8b4b8 45%,#6fc2cf 100%);color:#fff;text-align:center}
.login h2{font-family:"Quicksand",sans-serif;font-weight:600;font-size:18px;margin-top:17px}
.field{position:absolute;left:14px;width:188px;height:33px;background:#fff;border-radius:5px;color:#8a8a90;font-size:8.5px;text-align:left;padding:12px 12px}
.login .go{position:absolute;left:65px;top:162px;width:86px;height:28px;background:var(--blue);border-radius:5px;font-size:10px;display:flex;align-items:center;justify-content:center}
.login small{position:absolute;left:0;width:100%;font-size:8.5px}

.sec-title{font-size:26px;letter-spacing:.4px}
.arrow{position:absolute;width:31px;height:31px;border-radius:50%;border:2px solid var(--blue);display:flex;align-items:center;justify-content:center}
.arrow.off{border-color:#aec6ee}
.card{position:absolute;top:878px;width:250px;height:250px;border-radius:12px}

.lesson-copy{left:100px;top:1440px;width:445px;font-size:11px;line-height:20.5px}
.lesson-copy p{margin-bottom:11px}
.band{left:678px;top:1377px;width:522px;height:368px;background:var(--band)}
.photo{position:absolute;top:1406px;height:269px;border-radius:14px}

.center{left:0;width:1200px;text-align:center}
.video{left:275px;top:2046px;width:650px;height:364px;border-radius:16px;background:linear-gradient(135deg,#8f8d88,#c9c6bd 45%,#6f6a62)}
.play{left:563px;top:2200px;width:76px;height:54px;border-radius:12px;background:rgba(30,30,30,.8);display:flex;align-items:center;justify-content:center}

.foot-col h4{font-weight:400;font-size:14px;color:var(--ink);margin-bottom:18px}
.foot-col a,.foot-col p{display:block;font-size:11px;color:var(--ink);margin-bottom:13px}
.email{left:861px;top:2898px;width:203px;height:27px;border:1.5px solid var(--blue);border-radius:14px}
.email span{position:absolute;left:26px;top:-7px;font-size:7px;color:var(--blue);background:var(--foot);padding:0 3px}
.email b{position:absolute;right:2px;top:2px;width:58px;height:20px;border-radius:10px;background:var(--green);color:#fff;font-size:8px;display:flex;align-items:center;justify-content:center}
</style>
</head>
<body>
<div class="page">

  <div class="abs brand">Brightwick</div>
  <nav class="menu">
    <a style="left:250px">Home</a>
    <a style="left:315px" class="active">Courses</a>
    <a style="left:390px">Programms</a>
    <a style="left:485px">Team</a>
    <a style="left:546px">Contact</a>
  </nav>
  <a class="btn btn-outline" style="left:861px;top:31px;width:108px;height:35px">Login</a>
  <a class="btn btn-solid" style="left:979px;top:31px;width:120px;height:35px">Sign Up</a>

  <h1 class="abs head hero-title">Experience <span class="accent">breacktrough</span><br>Learning with<br><span class="accent">Brightwick</span> Education</h1>
  <div class="abs hero-copy">
    <p>Experience breakthrough learning with a platform that offers Grade 4-12 CAPS curriculum Maths and Science training through personal, interactive sessions at any pace.</p>
    <p>Watch tutorials and get in touch with educators including group chats to post your questions. Choose from a variety of question sheets and quizzes to test your knowledge as you go.</p>
  </div>
  <a class="btn btn-green" style="left:100px;top:514px;width:167px;height:34px;font-size:11px">Join live sessions</a>
  <a class="abs learn-link">Learn more about us
    <svg width="12" height="10" viewBox="0 0 12 10"><path d="M0 5h10M6 1l4 4-4 4" stroke="#1459d9" stroke-width="1.3" fill="none"/></svg></a>
  <div class="abs stat">1.3K</div>
  <div class="abs avatars" role="img" aria-label="Profile photos of learners">
    <span style="background:#3c88c9"></span><span style="background:#1f1f24"></span><span style="background:#7a6f6a"></span><span style="background:#e98fa0"></span><span style="background:#d7354a"></span><span style="background:#c72d2d"></span><span style="background:#9d8cd8"></span>
  </div>

  <svg class="abs" style="left:630px;top:125px" width="540" height="545" viewBox="0 0 540 545">
    <circle cx="275" cy="280" r="262" fill="none" stroke="#555" stroke-width="1.6" stroke-dasharray="3 6"/>
  </svg>
  <div class="abs hero-photo" role="img" aria-label="Photo of a smiling tutor holding a laptop"></div>

  <div class="badge" style="left:1014px;top:163px;background:#7ef0a0">
    <svg width="20" height="20" viewBox="0 0 20 20"><path d="M4 17h12M8 17V9l5-5 2 2-5 5" stroke="#12b640" stroke-width="2" fill="none"/></svg></div>
  <div class="badge" style="left:622px;top:498px;background:#c78bf5">
    <svg width="20" height="20" viewBox="0 0 20 20" stroke="#7a1fd0" stroke-width="1.8" fill="none"><path d="M3 5h5M12 5h6M15 2v6M3 12l4 4M7 12l-4 4M12 13h6M12 16h6"/></svg></div>
  <div class="badge" style="left:740px;top:610px;background:#8fa4f7">
    <svg width="20" height="20" viewBox="0 0 20 20" stroke="#2341c8" stroke-width="1.8" fill="none"><circle cx="7" cy="7" r="4"/><circle cx="13" cy="13" r="4"/></svg></div>

  <form class="abs login">
    <h2>Login</h2>
    <div class="field" style="top:65px">Email / Mobile Number</div>
    <div class="field" style="top:113px">Password</div>
    <div class="go">Login</div>
    <small style="top:207px">Forgot your password?</small>
    <small style="top:229px">Create an account</small>
  </form>

  <h2 class="abs head sec-title" style="left:101px;top:784px">Join Our <span class="accent">Courses</span></h2>
  <div class="arrow off" style="left:1024px;top:786px"><svg width="10" height="12" viewBox="0 0 10 12"><path d="M7 1L2 6l5 5" stroke="#aec6ee" stroke-width="1.6" fill="none"/></svg></div>
  <div class="arrow" style="left:1068px;top:786px"><svg width="10" height="12" viewBox="0 0 10 12"><path d="M3 1l5 5-5 5" stroke="#1459d9" stroke-width="1.6" fill="none"/></svg></div>

  <div class="card" style="left:100px;background:linear-gradient(160deg,#c8e7ef,#9fd3e3)" role="img" aria-label="Grade 8, 10 and 12 natural and physical science course poster with books"></div>
  <div class="card" style="left:390px;background:linear-gradient(160deg,#4a4a4a,#2e2e2e)" role="img" aria-label="Grade 7, 9 and 11 mathematics course poster on chalkboard"></div>
  <div class="card" style="left:681px;background:linear-gradient(180deg,#f0f0f0 0 38%,#ee3e34 42%,#e8392f)" role="img" aria-label="Grade 8, 10 and 12 mathematics course poster with book stack"></div>
  <div class="card" style="left:972px;background:linear-gradient(160deg,#3f6e50,#2c5039)" role="img" aria-label="Grade 7, 9 and 11 science course poster on green chalkboard"></div>

  <a class="btn btn-outline" style="left:489px;top:1191px;width:221px;height:44px;border-radius:8px;font-weight:400">See all courses</a>

  <h2 class="abs head sec-title" style="left:101px;top:1374px"><span class="accent">Lessons</span> With Benefits</h2>
  <div class="abs lesson-copy">
    <p>Brightwick Education is a zero-rated site which means that Telnova does not charge data costs to use the site.</p>
    <p>Up to 4 Learners can register for every Telnova customer account</p>
    <p>Brightwick Education is a mobile-friendly platform with plenty of videos and resources, creating an engaging environment for students who may need to refresh certain parts of the curriculum.</p>
    <p>Do online quizzes to track progress.</p>
  </div>
  <a class="btn btn-solid" style="left:100px;top:1663px;width:139px;height:34px;font-size:11px;font-weight:400">Learn more</a>

  <div class="abs band"></div>
  <div class="photo" style="left:600px;width:406px;background:linear-gradient(135deg,#6b5a4c,#b9ada0 50%,#4d3f35)" role="img" aria-label="Learners studying together at a laptop"></div>
  <div class="photo" style="left:1034px;width:190px;background:linear-gradient(135deg,#e8e8ea,#cfcfd4)" role="img" aria-label="Tutor presenting at a whiteboard screen"></div>
  <div class="arrow off" style="left:694px;top:1701px;border-color:#9fb6e0"><svg width="10" height="12" viewBox="0 0 10 12"><path d="M7 1L2 6l5 5" stroke="#9fb6e0" stroke-width="1.6" fill="none"/></svg></div>
  <div class="arrow" style="left:738px;top:1701px;border-color:#1f4fb8"><svg width="10" height="12" viewBox="0 0 10 12"><path d="M3 1l5 5-5 5" stroke="#1f4fb8" stroke-width="1.6" fill="none"/></svg></div>

  <h2 class="abs head center" style="top:1882px;font-size:28px;letter-spacing:.4px">The <span class="accent">Modern</span> Learning <span class="accent">Experience</span></h2>
  <p class="abs center" style="top:1962px;font-size:11px;line-height:20.5px;padding:0 220px">Brightwick Learning Management System allows subject matter experts to engage with users using any internet connectable device. By focusing on digital content and interactivity Brightwick aims to make education more accessible to users everywhere.</p>
  <div class="abs video" role="img" aria-label="Intro video still: learner with headphones at a tablet, with cartoon students"></div>
  <div class="abs play"><svg width="22" height="24" viewBox="0 0 22 24"><path d="M2 1l19 11L2 23z" fill="#fff"/></svg></div>

  <a class="btn btn-green" style="left:236px;top:2474px;width:222px;height:45px;font-size:12px;font-weight:400">View how to videos</a>
  <a class="btn btn-solid" style="left:489px;top:2474px;width:222px;height:45px;font-size:12px;font-weight:400">Join our platform</a>
  <a class="btn btn-orange" style="left:742px;top:2474px;width:222px;height:45px;font-size:12px;font-weight:400">Learn more about us</a>

  <svg class="abs" style="left:0;top:2660px" width="1200" height="340" viewBox="0 0 1200 340" preserveAspectRatio="none">
    <path d="M0 60 C90 10 190 20 250 60 C330 110 480 120 560 70 C630 25 690 5 780 60 C880 120 980 80 1060 30 C1120 0 1170 20 1200 50 V340 H0Z" fill="var(--wave)"/>
    <path d="M0 120 C100 70 200 70 300 100 C420 140 480 140 560 115 C700 70 820 60 960 90 C1060 115 1140 110 1200 90 V340 H0Z" fill="var(--wave-light)"/>
    <path d="M0 135 C150 110 300 110 420 120 C600 130 760 95 900 100 C1030 105 1130 120 1200 115 V340 H0Z" fill="var(--foot)"/>
  </svg>

  <div class="abs" style="left:138px;top:2812px;font-family:'Quicksand',sans-serif;font-weight:700;font-size:30px;color:var(--blue-dark)">Brightwick</div>
  <p class="abs" style="left:135px;top:2882px;width:190px;font-size:9px;line-height:20px;color:var(--ink)">Experience breakthrough learning with a platform that offers Grade 4-12 CAPS curriculum Maths and Science training.</p>

  <div class="abs foot-col" style="left:388px;top:2800px">
    <h4>Brightwick</h4><a>Home</a><a>Courses</a><a>Programs</a><a>About</a>
  </div>
  <div class="abs foot-col" style="left:607px;top:2800px">
    <h4>Company</h4><a>Contact Us</a><a>Privacy Policy</a><a>Terms &amp; Conditions</a><a>Cookies</a>
  </div>
  <div class="abs foot-col" style="left:861px;top:2800px">
    <h4>Get in touch</h4><p style="margin-bottom:10px">Sign up to Brightwick Education</p><p>and never miss a session again</p>
  </div>
  <div class="abs email"><span>Enter your email</span><b>Sign Up</b></div>

</div>
</body>
</html>
```